Comets Business Card Design Project

Create a standard format for letterhead and business cards. I know I can just get the layout with an example name on it, then add the names, titles and address that we want to it and give that to a printer so that the graphics are much better. Organization Mission Statement: Providing a professionally organized, structured, and supportive environment with quality development and professional coaching to inspire our student athletes, and assist them in fulfilling their dreams of achievement in academic excellence, high level competition and playing collegiate softball. Girl's Elite Fastpitch Softball

Check web site: www.brookvalediamondcomets.org
Updates

Sorry I didn't get the URL and files out when I started the project. Logo examples, mission, vision, etc. are posted now. And the URL to the web site is www.brookvalediamondcomets.org.

I'm very interested in an original creative design that is professional yet relevant to a sports team and for coaches.

Target Market(s)

college recuriters, industry product suppliers, parents, coaches, tournament directors

Industry/Entity Type

Environment

Requirements
Must have
• Use one of two logos; include the web site URL and a general mailbox for inquires. Includes Name, title, email and phone number
Nice to have
• Some color variations or background. Maybe a mission statement on the back. Maybe a QR code to the web site.

```html
<!DOCTYPE html>
<html lang="en">
<head>
<meta charset="utf-8">
<title>Brookvale Comets – Business Cards</title>
<link rel="stylesheet" href="https://fonts.googleapis.com/css2?family=Cinzel:wght@500&family=Quicksand:wght@500;700&display=swap">
<style>
  :root {
    --page-bg: #2b2b2b;
    --ball-yellow: #cfc43a;
    --glove-brown: #8a7448;
    --wood-light: #ecd0a4;
    --wood-mid: #d9b486;
    --grass-dark: rgba(34, 44, 14, 0.75);
    --panel-white: rgba(255, 255, 255, 0.28);
    --text-white: #ffffff;
    --brand-red: #d8203f;
  }
  * { margin: 0; padding: 0; box-sizing: border-box; }
  html, body { width: 1200px; height: 1000px; overflow: hidden; }
  body {
    background: var(--page-bg);
    position: relative;
    font-family: "Quicksand", sans-serif;
  }
  .business-card {
    position: absolute;
    left: 202px;
    width: 805px;
    height: 440px;
    overflow: hidden;
  }
  .business-card--classic { top: 36px; }
  .business-card--state { top: 520px; }

  .card-photo {
    position: absolute;
    inset: 0;
    background:
      linear-gradient(180deg, rgba(0,0,0,0) 55%, var(--grass-dark) 100%),
      linear-gradient(100deg, var(--ball-yellow) 0%, #bdb238 34%, var(--glove-brown) 48%, var(--wood-mid) 60%, var(--wood-light) 82%, var(--wood-mid) 100%);
  }

  .contact-panel {
    position: absolute;
    left: 0;
    top: 220px;
    width: 336px;
    height: 174px;
    background: var(--panel-white);
    border-radius: 0 10px 10px 0;
    color: var(--text-white);
  }
  .coach-name {
    position: absolute;
    left: 24px;
    top: 20px;
    font-family: "Cinzel", serif;
    font-weight: 500;
    font-size: 24px;
    letter-spacing: 0.5px;
    line-height: 1;
  }
  .coach-title {
    position: absolute;
    right: 28px;
    top: 48px;
    font-size: 10px;
    letter-spacing: 2.5px;
    font-weight: 500;
  }
  .contact-list {
    position: absolute;
    left: 35px;
    top: 80px;
    list-style: none;
    font-size: 11px;
    line-height: 24px;
    font-weight: 500;
  }
  .contact-list b { font-weight: 700; }

  .team-mark {
    position: absolute;
    left: 462px;
    width: 320px;
    color: var(--brand-red);
    font-family: "Quicksand", sans-serif;
    font-weight: 700;
    font-size: 46px;
    line-height: 1.05;
  }
  .business-card--classic .team-mark { top: 140px; }
  .business-card--state .team-mark { top: 160px; }

  .website {
    position: absolute;
    right: 14px;
    bottom: 10px;
    color: var(--text-white);
    font-size: 12px;
    font-weight: 700;
    letter-spacing: 3.6px;
    text-transform: uppercase;
  }
</style>
</head>
<body>

  <article class="business-card business-card--classic">
    <div class="card-photo" role="img" aria-label="Close-up photo of a yellow softball resting in a leather glove beside a wooden bat on grass"></div>
    <section class="contact-panel">
      <h1 class="coach-name">Dana Whitfield</h1>
      <p class="coach-title">HEAD COACH</p>
      <ul class="contact-list">
        <li><b>Phone:</b> 555 240 7316</li>
        <li><b>Address:</b> 4410 Larkspur Lane Brookvale, OR 97000</li>
        <li><b>Email:</b> info@brookvalecomets.org</li>
      </ul>
    </section>
    <div class="team-mark">Brookvale<br>Comets</div>
    <p class="website">www.brookvalediamondcomets.org</p>
  </article>

  <article class="business-card business-card--state">
    <div class="card-photo" role="img" aria-label="Close-up photo of a yellow softball resting in a leather glove beside a wooden bat on grass"></div>
    <section class="contact-panel">
      <h1 class="coach-name">Dana Whitfield</h1>
      <p class="coach-title">HEAD COACH</p>
      <ul class="contact-list">
        <li><b>Phone:</b> 555 240 7316</li>
        <li><b>Address:</b> 4410 Larkspur Lane Brookvale, OR 97000</li>
        <li><b>Email:</b> info@brookvalecomets.org</li>
      </ul>
    </section>
    <div class="team-mark">Brookvale Comets</div>
    <p class="website">www.brookvalediamondcomets.org</p>
  </article>

</body>
</html>
```